依頼詳細
現サイト:http://www.rmb.ac.jp/nyushi/

参考サイト(クライアント様が元気でいいなと感じているサイト):http://hoshizora.jp/

ご要望は「大胆さ、元気で明るい高専生活が待っている!」と感じていただけるデザイン。(むずかしくてすいません…)
画像、ロゴマークに関しては下記サイトの中にあるもの全て使用可能です。(適切なサイズをご使用ください)
www.rmb.ac.jp/nyushi/
http://www.rmb.ac.jp/

※選定するのは弊社ではなく、クライアント様でございますので、コンペ終了日より数日のお返事(ご当選)となってしまいますが御了承くださいませ。
サイトURL
http://www.rmb.ac.jp/nyushi/
ページ数
1ページ
希望イメージ
シンプル 複雑
単色 カラフル
暗い 明るい
日常 高級
遊び心 厳粛
未来的 伝統的
女性的 男性的
希望する色
多色とシンプルの中間といったところでしょうか。
納品ファイル
• フォトショップ形式 (.psd)
• PNG形式 (.png)
補足説明
制作にあたり、写真の使用で生徒さんの顔が写っているものがありますが、すべて使用可能ということです。
■ 選んだ理由

選定にお時間をいただき、ありがとうございます。
クライアント様がお選びになりました。

■ 提案者全員のお礼・コメント

大変お時間をいただき、ありがとうございました。
また機会があればよろしくお願い申し上げます。

株式会社ミナ
森下

```html
<!DOCTYPE html>
<html lang="ja">
<head>
<meta charset="utf-8">
<title>緑峰工業高等専門学校 入試情報</title>
<link href="https://fonts.googleapis.com/css2?family=Noto+Sans+JP:wght@400;700&display=swap" rel="stylesheet">
<style>
:root{
  --blue:#2aa5dc;
  --blue-dark:#1b86bb;
  --blue-pale:#d7eef9;
  --green:#8cc63f;
  --orange:#f08c1e;
  --orange-pale:#fdebd6;
  --yellow-pale:#f3f7d2;
  --text:#333;
  --white:#fff;
  --photo-a:#b9c9d4;
  --photo-b:#8fb07a;
}
*{box-sizing:border-box;margin:0;padding:0}
html,body{width:791px;height:1200px;overflow:hidden;background:var(--white);font-family:"Noto Sans JP",sans-serif;color:var(--text)}
.desktop,.mobile{position:absolute;top:0;overflow:hidden}
.desktop{left:0;width:512px;height:712px}
.mobile{left:525px;width:266px;height:1200px}
.brand{display:flex;align-items:center;gap:5px;font-weight:700;color:var(--blue-dark)}
.brand .mark{width:14px;height:14px;border-radius:50%;background:var(--blue)}
.brand small{display:block;font-size:5px;font-weight:400;letter-spacing:.5px}
.photo{background:linear-gradient(135deg,var(--photo-a),#e6ecef 60%,var(--photo-b))}
.dots{display:flex;justify-content:center;gap:5px;padding:6px 0}
.dots i{width:5px;height:5px;border-radius:50%;background:#ccc}
.dots i:first-child{background:var(--blue)}

/* desktop */
.d-header{height:56px;display:flex;align-items:center;justify-content:space-between;padding:0 18px;border-bottom:3px solid var(--blue)}
.d-header .brand{font-size:10px}
.d-nav{display:flex;gap:4px;align-items:center}
.d-nav a{font-size:7px;color:var(--text);text-decoration:none;padding:4px 6px}
.d-nav .cta{background:var(--green);color:var(--white);border-radius:2px}
.d-hero{position:relative;height:190px}
.d-hero .band{position:absolute;left:60px;right:60px;top:118px;background:rgba(42,165,220,.85);color:var(--white);padding:7px 12px;font-size:11px;font-weight:700}
.d-hero .band small{display:block;font-size:6px;font-weight:400}
.d-open{margin:6px auto 12px;width:260px;border:2px solid var(--orange);text-align:center;padding:6px 0}
.d-open small{display:block;font-size:7px;color:var(--orange)}
.d-open strong{display:block;margin-top:3px;background:var(--orange);color:var(--white);font-size:11px;padding:4px 0;margin-left:8px;margin-right:8px}
.d-life{background:var(--blue-pale);padding:16px 0 14px}
.d-life h2{text-align:center;font-size:12px;color:var(--blue-dark);margin-bottom:12px}
.d-cards{display:flex;justify-content:center;gap:10px}
.d-card{width:150px}
.d-card .photo{height:88px}
.d-card p{color:var(--white);font-size:8px;font-weight:700;padding:6px 8px}
.d-card p small{display:block;font-size:5px;font-weight:400}
.green{background:var(--green)}
.bluebg{background:var(--blue)}
.d-links{display:flex;justify-content:center;gap:22px;padding:14px 0}
.d-link{display:flex;gap:5px;align-items:center;width:100px;font-size:7px;font-weight:700}
.d-link i{width:18px;height:18px;border-radius:50%;flex:none}
.d-link small{display:block;font-size:5px;font-weight:400;color:#777}
.d-foot{background:var(--blue);color:var(--white);font-size:6px;padding:12px 40px;height:58px}
.d-foot-sub{background:var(--blue-dark);color:var(--white);font-size:5px;text-align:center;padding:6px 0}

/* mobile */
.m-header{height:45px;display:flex;align-items:center;justify-content:space-between;padding:0 8px}
.m-header .brand{font-size:9px}
.m-header .cta{background:var(--green);color:var(--white);font-size:7px;padding:4px 6px;border-radius:2px}
.m-hero{position:relative;height:178px}
.m-hero .band{position:absolute;left:0;right:0;bottom:14px;background:rgba(42,165,220,.85);color:var(--white);font-size:8px;font-weight:700;padding:5px 8px;line-height:1.4}
.m-open{background:var(--orange);color:var(--white);font-size:9px;font-weight:700;text-align:center;padding:5px 0}
.m-dates{font-size:7px;line-height:1.6;padding:6px 14px 10px}
.m-card .photo{height:104px}
.m-card p{color:var(--white);font-size:10px;font-weight:700;padding:8px 12px;height:62px}
.m-card p small{display:block;font-size:6px;font-weight:400;margin-top:3px}
.m-list{padding:8px 0 0}
.m-item{display:flex;align-items:center;gap:10px;padding:8px 12px;height:72px;margin-bottom:4px;font-size:9px;font-weight:700}
.m-item i{width:30px;height:30px;border-radius:50%;flex:none}
.m-item small{display:block;font-size:6px;font-weight:400;color:#666}
.pagetop{background:var(--blue-pale);color:var(--blue-dark);font-size:7px;text-align:right;padding:6px 10px;margin-top:6px}
.m-foot{background:var(--blue);color:var(--white);padding:14px 12px;height:240px;font-size:6px;line-height:1.6}
.m-foot .brand{color:var(--white);font-size:9px;margin-bottom:6px}
.m-foot .brand .mark{background:var(--white)}
</style>
</head>
<body>

<section class="desktop">
  <header class="d-header">
    <div class="brand"><span class="mark"></span><div>緑峰工業高等専門学校<small>RYOKUHO TECHNICAL COLLEGE</small></div></div>
    <nav class="d-nav"><a>入試情報</a><a>学校案内</a><a>学科紹介</a><a>学校生活</a><a>アクセス</a><a class="cta">資料請求</a></nav>
  </header>
  <div class="d-hero photo" role="img" aria-label="実習室で学ぶ学生たちの写真">
    <div class="band"><small>平成29年度</small>OpenCampus 日程</div>
  </div>
  <div class="dots"><i></i><i></i><i></i><i></i></div>
  <div class="d-open"><small>平成29年度入試向け</small><strong>OpenCampus 日程</strong></div>
  <section class="d-life">
    <h2>緑峰工業高等専門学校での生活</h2>
    <div class="d-cards">
      <div class="d-card"><div class="photo" role="img" aria-label="屋外イベントの写真"></div><p class="green">緑峰高専のイベント<small>体育祭や文化祭など年間行事の紹介</small></p></div>
      <div class="d-card"><div class="photo" role="img" aria-label="学生の集合写真"></div><p class="bluebg">緑峰高専生の学校生活<small>授業や部活動など毎日の様子</small></p></div>
    </div>
  </section>
  <div class="d-links">
    <div class="d-link"><i style="background:var(--orange)"></i><div>入試情報<small>募集要項はこちら</small></div></div>
    <div class="d-link"><i style="background:var(--blue)"></i><div>緑峰高専の施設<small>校内設備の紹介</small></div></div>
    <div class="d-link"><i style="background:var(--green)"></i><div>資料請求<small>案内資料の請求</small></div></div>
  </div>
  <footer class="d-foot">緑峰工業高等専門学校<br>〒000-0000 緑峰市星が丘3番町2番地 TEL 0000-12-3456</footer>
  <div class="d-foot-sub">COPYRIGHT © RYOKUHO TECHNICAL COLLEGE</div>
</section>

<section class="mobile">
  <header class="m-header">
    <div class="brand"><span class="mark"></span><div>緑峰工業高等専門学校<small>RYOKUHO TECHNICAL COLLEGE</small></div></div>
    <span class="cta">入試情報</span>
  </header>
  <div class="m-hero photo" role="img" aria-label="実習室で学ぶ学生たちの写真">
    <div class="band">平成29年度 OpenCampus<br>第1回 実習を体験しよう!(専門科目)</div>
  </div>
  <div class="dots"><i></i><i></i><i></i><i></i></div>
  <div class="m-open">平成29年度入試向け OpenCampus 日程</div>
  <p class="m-dates">第1回 6/4(日) 実習を体験しよう!<br>第2回 8/27 第3回 10/22・23 第4回 11/12<br>第5回 12/10</p>
  <div class="m-card"><div class="photo" role="img" aria-label="屋外イベントの写真"></div><p class="green">緑峰高専のイベント<small>体育祭や文化祭など年間行事の様子を紹介しています</small></p></div>
  <div class="m-card"><div class="photo" role="img" aria-label="学生の集合写真"></div><p class="bluebg">緑峰高専生の学校生活<small>授業や部活動など学生の毎日を紹介しています</small></p></div>
  <div class="m-list">
    <div class="m-item" style="background:var(--orange-pale)"><i style="background:var(--orange)"></i><div>入試情報<small>Admission Information<br>各分野の入試情報はこちら</small></div></div>
    <div class="m-item" style="background:var(--blue-pale)"><i style="background:var(--blue)"></i><div>緑峰高専の施設<small>Facility<br>校内設備の紹介はこちら</small></div></div>
    <div class="m-item" style="background:var(--yellow-pale)"><i style="background:var(--green)"></i><div>資料請求<small>Request<br>案内資料の請求はこちら</small></div></div>
  </div>
  <div class="pagetop">PageTop ▲</div>
  <footer class="m-foot">
    <div class="brand"><span class="mark"></span>緑峰工業高等専門学校</div>
    〒000-0000 緑峰市星が丘3番町2番地<br>TEL 0000-12-3456 / FAX 0000-12-3457<br>RYOKUHO TECHNICAL COLLEGE<br><br>COPYRIGHT © RYOKUHO TECHNICAL COLLEGE
  </footer>
</section>

</body>
</html>
```